modernized upgrade to existing squarespace site

Hello! I have the following page for my consulting firm: https://fernwaystrategygroup.com/ Would love to upgrade to something more modern/attractive like here: https://www.lobrettiandco.com/ or https://quillbrightlab.com/ , but I am open to creativity. Would like to retain the logo look and color theme from the logo. The rest can be left to creative discretion.

```html
<!DOCTYPE html>
<html lang="en">
<head>
<meta charset="utf-8">
<title>Fernway Strategy Group</title>
<link rel="stylesheet" href="https://fonts.googleapis.com/css2?family=Merriweather:wght@400;700&family=Open+Sans:wght@400;600&display=swap">
<style>
:root{
  --rose:#c68b80;
  --rose-text:#c4877c;
  --blush:#f3e6e5;
  --ink:#2b2b2b;
  --body:#3c3c3c;
  --muted:#6b6b6b;
  --stripe:#ececec;
  --white:#ffffff;
}
*{margin:0;padding:0;box-sizing:border-box}
html,body{width:1200px;height:2856px;overflow:hidden;background:var(--white)}
body{position:relative;font-family:"Open Sans",sans-serif;color:var(--body)}
.abs{position:absolute}
.serif{font-family:"Merriweather",serif}

/* header */
.brand{display:flex;align-items:center;gap:12px}
.brand-square{width:42px;height:42px;border:2px solid var(--rose)}
.brand-name{font-family:"Merriweather",serif;font-size:19px;color:var(--ink);letter-spacing:1px;line-height:1.2}
.nav{top:43px;left:495px;display:flex;gap:19px;font-size:15px;color:var(--ink)}
.social{font-size:13px;color:var(--ink);font-weight:600}
.btn-rose{background:var(--rose);color:var(--white);font-weight:600;font-size:15px;display:flex;align-items:center;justify-content:center;border-radius:3px}
.btn-dark{background:#000;color:var(--white);font-weight:600;font-size:15px;display:flex;align-items:center;justify-content:center;border-radius:3px}

/* hero */
.hero{top:103px;left:0;width:1200px;height:428px;background:linear-gradient(160deg,#4a4f5c 0%,#7a6a58 40%,#8e7254 65%,#3f3a36 100%)}
.hero-title{top:200px;left:0;width:1200px;text-align:center;color:var(--white);font-family:"Merriweather",serif;font-size:56px;line-height:61px}
.hero-sub{top:333px;left:0;width:1200px;text-align:center;color:var(--white);font-family:"Merriweather",serif;font-size:27px}

.feature-title{font-family:"Merriweather",serif;font-weight:700;font-size:35px;line-height:44px;color:var(--ink)}
.feature-title em{font-style:normal;color:var(--rose-text)}
.photo{border:1px solid #ddd}
.stripes{background:var(--stripe)}

/* services */
.services{top:1543px;left:0;width:1200px;height:540px;background:var(--blush)}
.section-title{width:1200px;left:0;text-align:center;font-family:"Merriweather",serif;font-weight:700;font-size:36px;color:var(--ink)}
.service{width:280px;text-align:center}
.service svg{display:block;margin:0 auto}
.service h3{font-family:"Merriweather",serif;font-weight:400;font-size:22px;line-height:31px;color:var(--ink);margin-top:30px}
.service p{font-size:15px;line-height:27.5px;color:var(--body);margin-top:14px}

/* press */
.press{font-family:"Merriweather",serif;font-weight:700;color:#5a5a5a;font-size:24px;text-align:center;display:flex;align-items:center;justify-content:center;line-height:1.2}

/* footer */
.footer{top:2580px;left:0;width:1200px;height:276px;background:var(--blush)}
.foot-head{font-size:14px;font-weight:600;color:var(--ink);letter-spacing:.3px}
.foot-links{list-style:none;font-size:14.5px;color:var(--ink);line-height:28.5px;margin-top:8px}
</style>
</head>
<body>

<header>
  <div class="abs brand" style="top:30px;left:111px">
    <div class="brand-square"></div>
    <div class="brand-name">Fernway Strategy Group</div>
  </div>
  <nav class="abs nav">
    <span>Home</span><span>Services</span><span>Research</span><span>The Institute</span><span>In the News</span>
  </nav>
  <div class="abs social" style="top:44px;left:916px">Postline</div>
  <div class="abs btn-rose" style="top:33px;left:973px;width:115px;height:38px">Get Started</div>
</header>

<section>
  <div class="abs hero" role="img" aria-label="Upward view of city office towers against the sky"></div>
  <h1 class="abs hero-title">Macroeconomic<br>&amp; policy analytics</h1>
  <p class="abs hero-sub">for today’s turbulent environment.</p>
  <div class="abs btn-rose" style="top:396px;left:542px;width:116px;height:40px">Get Started</div>
</section>

<section>
  <h2 class="abs feature-title" style="top:668px;left:110px;width:480px">Sophisticated research &amp; atypical analyses <em>for improved communications.</em></h2>
  <div class="abs btn-dark" style="top:829px;left:110px;width:124px;height:39px">Learn More</div>
  <div class="abs stripes" style="top:850px;left:990px;width:159px;height:158px"></div>
  <div class="abs photo" role="img" aria-label="Team meeting around a table with a presenter at a flip chart" style="top:600px;left:644px;width:444px;height:345px;background:linear-gradient(135deg,#c9ccd0 0%,#e9e6e1 45%,#b59a7a 100%)"></div>
</section>

<section>
  <div class="abs stripes" style="top:1303px;left:51px;width:159px;height:159px"></div>
  <div class="abs photo" role="img" aria-label="Hands reviewing financial charts on a laptop and paper reports" style="top:1054px;left:111px;width:444px;height:345px;background:linear-gradient(135deg,#d8d9dc 0%,#eeeeec 45%,#8f8b86 100%)"></div>
  <h2 class="abs feature-title" style="top:1122px;left:640px;width:480px">Proprietary public relations tools that <em>guarantee media visibility</em>.</h2>
  <div class="abs btn-dark" style="top:1283px;left:640px;width:124px;height:38px">Learn More</div>
</section>

<section>
  <div class="abs services"></div>
  <h2 class="abs section-title" style="top:1612px">What we do</h2>

  <div class="abs service" style="top:1711px;left:102px">
    <svg width="70" height="70" viewBox="0 0 70 70" fill="none" stroke="#c4877c" stroke-width="2.5">
      <rect x="3" y="3" width="64" height="64" rx="3"/><line x1="3" y1="15" x2="67" y2="15"/>
      <rect x="14" y="44" width="8" height="17"/><rect x="30" y="36" width="8" height="25"/><rect x="46" y="40" width="8" height="21"/>
      <polyline points="10,38 24,26 38,32 58,20"/>
    </svg>
    <h3>Analytics &amp;<br>Messaging</h3>
    <p>Our communications team can develop influential messaging, in conjunction with our data scientists’ technical expertise.</p>
  </div>

  <div class="abs service" style="top:1711px;left:462px">
    <svg width="70" height="70" viewBox="0 0 70 70" fill="none" stroke="#c4877c" stroke-width="2.5">
      <path d="M4 3h40l14 14v50H4z"/><circle cx="22" cy="22" r="10"/><path d="M22 12v10h10"/>
      <rect x="16" y="46" width="7" height="15"/><rect x="30" y="38" width="7" height="23"/><rect x="44" y="42" width="7" height="19"/>
    </svg>
    <h3>Customized<br>Reports</h3>
    <p>From succinct summations of economic and policy impact to full-length analyses, we can create the customized exposition that best represents your interests.</p>
  </div>

  <div class="abs service" style="top:1711px;left:820px">
    <svg width="70" height="70" viewBox="0 0 70 70" fill="none" stroke="#c4877c" stroke-width="2.5">
      <rect x="14" y="6" width="46" height="58" rx="3"/><rect x="28" y="2" width="18" height="8"/>
      <polyline points="22,22 26,26 32,18"/><line x1="36" y1="22" x2="52" y2="22"/>
      <polyline points="22,36 26,40 32,32"/><line x1="36" y1="36" x2="52" y2="36"/>
      <circle cx="12" cy="50" r="6"/><path d="M2 68c0-8 4-11 10-11s10 3 10 11"/>
    </svg>
    <h3>Proprietary<br>Surveys</h3>
    <p>Exclusive, custom-designed surveys can enrich your databank, while maintaining access to proprietary resources, establishing you and your firm as a thought leader.</p>
  </div>
</section>

<section>
  <h2 class="abs section-title" style="top:2148px">As seen on</h2>
  <div class="abs press" style="top:2257px;left:112px;width:160px;height:100px">Meridian Weekly</div>
  <div class="abs press" style="top:2257px;left:300px;width:160px;height:100px">Harbor News</div>
  <div class="abs press" style="top:2257px;left:492px;width:160px;height:100px">Crestline News</div>
  <div class="abs press" style="top:2257px;left:700px;width:190px;height:100px">Ledgerpoint Finance</div>
  <div class="abs press" style="top:2257px;left:920px;width:170px;height:100px">Axial Business</div>
  <div class="abs press" style="top:2397px;left:420px;width:200px;height:120px">Open Air Radio</div>
  <div class="abs press" style="top:2397px;left:650px;width:150px;height:120px">The Capitol Desk</div>
</section>

<footer>
  <div class="abs footer"></div>
  <div class="abs brand" style="top:2645px;left:110px">
    <div class="brand-square" style="width:68px;height:68px"></div>
    <div class="brand-name" style="font-size:25px">Fernway Strategy Group</div>
  </div>
  <p class="abs" style="top:2765px;left:109px;font-size:15px;color:var(--ink)">2024 Fernway Strategy Group. All Rights Reserved.</p>

  <div class="abs" style="top:2650px;left:579px">
    <div class="foot-head">QUICK LINKS</div>
    <ul class="foot-links"><li>Home</li><li>Services</li><li>Research</li><li>The Institute</li></ul>
  </div>
  <div class="abs" style="top:2650px;left:811px">
    <div class="foot-head">OTHER LINKS</div>
    <ul class="foot-links"><li>In the News</li><li>Contact</li><li>Privacy Policy</li><li>Terms &amp; Conditions</li></ul>
  </div>
  <div class="abs social" style="top:2656px;left:1030px">Postline</div>
</footer>

</body>
</html>
```